furniture and home contents restoration

I need to list the services that we perform in our studio.
we serve the general public as well as the insurance/ remediation industry

```html
<!DOCTYPE html>
<html lang="en">
<head>
<meta charset="utf-8">
<title>Keystone Refinishers – Business Card</title>
<link href="https://fonts.googleapis.com/css2?family=Noto+Serif:wght@400;700&display=swap" rel="stylesheet">
<style>
  :root {
    --ink: #1f323d;
    --paper: #ffffff;
    --backdrop: #d9d6d1;
    --on-dark: #f2f4f5;
  }
  * { box-sizing: border-box; margin: 0; padding: 0; }
  html, body { width: 1200px; height: 930px; overflow: hidden; }
  body {
    background: var(--backdrop);
    font-family: "Noto Serif", Georgia, serif;
    position: relative;
  }
  .card {
    position: absolute;
    left: 250px;
    width: 700px;
    height: 400px;
    border-radius: 22px;
    overflow: hidden;
  }
  /* Back side */
  .card-back {
    top: 45px;
    background: var(--ink);
    color: var(--on-dark);
    padding: 34px 40px 30px;
    text-transform: uppercase;
  }
  .services-title {
    text-align: center;
    font-weight: 700;
    font-size: 22px;
    letter-spacing: 0.5px;
    margin-bottom: 22px;
  }
  .service-columns {
    display: flex;
    gap: 26px;
  }
  .service-list {
    list-style: none;
    font-size: 11.5px;
    line-height: 19px;
    flex: 1;
  }
  .service-list li::before {
    content: "•";
    margin-right: 6px;
  }
  .back-footer {
    position: absolute;
    left: 0; right: 0; bottom: 32px;
    text-align: center;
    font-size: 15px;
    line-height: 22px;
  }
  /* Front side */
  .card-front {
    top: 485px;
    background: var(--paper);
    color: var(--ink);
  }
  .company-name {
    position: absolute;
    left: 42px; top: 38px;
    font-weight: 700;
    font-size: 34px;
    line-height: 36px;
    text-transform: uppercase;
  }
  .person-name {
    position: absolute;
    right: 52px; top: 52px;
    font-weight: 700;
    font-size: 19px;
    text-transform: uppercase;
  }
  .name-mark {
    position: absolute;
    right: 20px; top: 56px;
    width: 18px; height: 18px;
    background: var(--ink);
  }
  .tagline {
    position: absolute;
    left: 42px; top: 190px;
    font-size: 15px;
    line-height: 19px;
    width: 300px;
  }
  .contact-list {
    position: absolute;
    left: 42px; top: 245px;
    list-style: none;
    font-size: 15px;
    line-height: 24px;
  }
  .contact-list li { display: flex; align-items: center; gap: 8px; }
  .contact-list svg { width: 12px; height: 12px; flex: none; }
</style>
</head>
<body>

<section class="card card-back">
  <h2 class="services-title">Home Contents Restoration</h2>
  <div class="service-columns">
    <ul class="service-list">
      <li>Antique repair and restoration</li>
      <li>Art cleaning and remounting</li>
      <li>Art and mirror frame repair</li>
      <li>Chandelier cleaning and restoration</li>
      <li>Document restoration</li>
      <li>Glass, ceramic, and mirror repair</li>
      <li>Hardware repair and restoration</li>
      <li>Kitchen removal and reinstallation</li>
      <li>Lamp cleaning and restoration</li>
      <li>Lamp shade replacement</li>
    </ul>
    <ul class="service-list">
      <li>Metal polishing and restoration</li>
      <li>Odor removal and ozone services</li>
      <li>Photo restoration</li>
      <li>Upholstery cleaning and deodorizing</li>
      <li>In-house upholstery and reupholstery</li>
      <li>Rug cleaning and restoration</li>
      <li>Musical instrument restoration</li>
      <li>Window treatment repair/ restoration</li>
      <li>Leather restoration and replacement</li>
      <li>Piano restoration and repair</li>
    </ul>
  </div>
  <p class="back-footer">On-site inspections and desk review services<br>Assessment reports and estimates for repair and restoration</p>
</section>

<section class="card card-front">
  <h1 class="company-name">Keystone<br>Refinishers</h1>
  <p class="person-name">Daniel Moretti</p>
  <span class="name-mark"></span>
  <p class="tagline">serving the general public and the insurance industry for over 40 years</p>
  <ul class="contact-list">
    <li><svg viewBox="0 0 12 12"><path fill="var(--ink)" d="M2.5 1l2 2.2-1 1.3a6 6 0 0 0 4 4l1.3-1 2.2 2-1.2 1.5C5 11 1 7 1 2.2z"/></svg>555 010 2400</li>
    <li><svg viewBox="0 0 12 12"><rect x="3" y="0.8" width="6" height="10.4" rx="1" fill="none" stroke="var(--ink)" stroke-width="1.2"/><circle cx="6" cy="9.4" r="0.7" fill="var(--ink)"/></svg>555 010 7731</li>
    <li><svg viewBox="0 0 12 12"><rect x="3" y="1" width="6" height="4" fill="none" stroke="var(--ink)"/><rect x="1" y="5" width="10" height="5" rx="1" fill="var(--ink)"/></svg>555 010 2640</li>
    <li><svg viewBox="0 0 12 12"><path fill="var(--ink)" d="M6 0.5a4 4 0 0 0-4 4c0 3 4 7 4 7s4-4 4-7a4 4 0 0 0-4-4zm0 5.6a1.6 1.6 0 1 1 0-3.2 1.6 1.6 0 0 1 0 3.2z"/></svg>12 elm hollow rd. riverton, ny 10000</li>
    <li><svg viewBox="0 0 12 12"><rect x="0.8" y="2.3" width="10.4" height="7.4" fill="none" stroke="var(--ink)" stroke-width="1.1"/><path d="M1 2.6l5 4 5-4" fill="none" stroke="var(--ink)" stroke-width="1.1"/></svg>studio@keystonerefinish.com</li>
  </ul>
</section>

</body>
</html>
```